Flyer for Lawnmowing and gardening business

We are a lawn mowing and gardening business needing a flyer designed listing our services and business info.
The flyer should include all business information and contact details as below.

Lawn mowing
Gardening
Green waste removal
Pruning
Weeding
Vegetable Garden Creation

Phone number:0457302864

As well as the logo provided

Target Market(s)

Local people wanting someone to care for their garden.

Industry/Entity Type

Gardener

Font styles to use
Serif

Requirements
Must have
• Business Logo
• All business info and services provided. EG
• Lawn mowing
• Gardening
• Green waste removal
• Pruning
• Weeding
• Vegetable Garden Creation
• Phone number:0457302864
Nice to have
• Earthy tones, clean and simple flyer design

```html
<!DOCTYPE html>
<html lang="en">
<head>
<meta charset="utf-8">
<title>Brookhaven – Services Flyer</title>
<link href="https://fonts.googleapis.com/css2?family=Goudy+Bookletter+1911&family=Libre+Baskerville&display=swap" rel="stylesheet">
<style>
  :root {
    --bg: #d5e9cf;
    --lime: #7be63a;
    --lime-soft: #a6ee6c;
    --lime-pale: #c8f59e;
    --heading-green: #6fdc3a;
    --number-green: #3f8f1c;
    --ink: #2f2018;
    --card-top: #ffffff;
    --card-bottom: #e3f1dc;
  }
  html, body {
    margin: 0;
    padding: 0;
    overflow: hidden;
  }
  .flyer {
    position: relative;
    width: 928px;
    height: 1200px;
    overflow: hidden;
    background:
      radial-gradient(ellipse 520px 170px at 240px 170px, rgba(255,255,255,0.95), rgba(255,255,255,0) 100%),
      linear-gradient(180deg, var(--bg) 0px, #eef7ea 60px, #fafdf8 150px, #f3f9f0 220px, var(--bg) 330px, var(--bg) 100%);
    font-family: "Goudy Bookletter 1911", Georgia, serif;
  }
  .edge-stripe {
    position: absolute;
    left: 0;
    width: 100%;
    height: 10px;
    display: flex;
  }
  .edge-stripe span { flex: 1; }
  .edge-stripe span:nth-child(odd) { background: var(--lime); }
  .edge-stripe span:nth-child(4n+2) { background: var(--lime-soft); }
  .edge-stripe span:nth-child(4n) { background: var(--lime-pale); }
  .edge-stripe.top { top: 0; }
  .edge-stripe.bottom { bottom: 0; }

  .brand {
    position: absolute;
    left: 444px;
    top: 53px;
    width: 457px;
    height: 226px;
    display: flex;
    align-items: center;
    justify-content: center;
    gap: 14px;
    white-space: nowrap;
  }
  .brand-mark {
    width: 22px;
    height: 22px;
    background: var(--ink);
  }
  .brand-name {
    font-size: 44px;
    color: var(--ink);
    letter-spacing: 2px;
  }

  .services-title {
    position: absolute;
    left: 31px;
    top: 352px;
    margin: 0;
    font-weight: 400;
    font-size: 44px;
    letter-spacing: -1px;
    color: var(--heading-green);
  }
  .services-rule {
    position: absolute;
    left: 0;
    top: 398px;
    width: 100%;
    height: 1px;
    background: var(--lime);
  }

  .service-list {
    list-style: none;
    margin: 0;
    padding: 0;
  }
  .service-card {
    position: absolute;
    width: 399px;
    display: flex;
    align-items: center;
    justify-content: flex-end;
    box-sizing: border-box;
    padding-right: 8px;
    border-radius: 0 0 10px 10px;
    border-bottom: 3px solid var(--lime-soft);
    background: linear-gradient(180deg, rgba(255,255,255,0) 0%, var(--card-top) 35%, var(--card-bottom) 100%);
    font-size: 37px;
    line-height: 31px;
    text-align: right;
    color: var(--ink);
  }
  .service-card .tuft {
    position: absolute;
    left: 0;
    bottom: 0;
    width: 50px;
    height: 78%;
    background: linear-gradient(180deg, rgba(166,238,108,0) 0%, var(--lime-soft) 45%, var(--lime) 100%);
    border-radius: 4px 4px 0 0;
  }
  .col-left { left: 31px; }
  .col-right { left: 495px; }
  .row-1 { top: 507px; height: 86px; }
  .row-2 { top: 634px; height: 106px; padding-top: 6px; }
  .row-3 { top: 788px; height: 84px; }

  .call-band {
    position: absolute;
    left: 0;
    top: 989px;
    width: 100%;
    height: 88px;
    box-sizing: border-box;
    border-top: 4px solid var(--lime-soft);
    border-bottom: 4px solid var(--lime-soft);
    background: radial-gradient(ellipse 300px 70px at 470px 50px, rgba(198,245,160,0.9), rgba(198,245,160,0) 100%), #dcefd5;
    display: flex;
    align-items: center;
    justify-content: center;
    gap: 28px;
    padding-left: 10px;
  }
  .call-label {
    font-size: 36px;
    letter-spacing: -1px;
    color: var(--heading-green);
  }
  .call-number {
    font-family: "Libre Baskerville", Georgia, serif;
    font-size: 38px;
    letter-spacing: 1px;
    color: var(--number-green);
    -webkit-text-stroke: 0.6px var(--number-green);
  }
</style>
</head>
<body>
<main class="flyer">
  <div class="edge-stripe top"><span></span><span></span><span></span><span></span><span></span><span></span><span></span><span></span></div>

  <header class="brand">
    <span class="brand-mark"></span>
    <span class="brand-name">BROOKHAVEN</span>
  </header>

  <h1 class="services-title">At your service for:</h1>
  <div class="services-rule"></div>

  <ul class="service-list">
    <li class="service-card col-left row-1"><span class="tuft" role="img" aria-label="Green grass tuft"></span>Lawn mowing</li>
    <li class="service-card col-right row-1"><span class="tuft" role="img" aria-label="Green grass tuft"></span>Gardening</li>
    <li class="service-card col-left row-2"><span class="tuft" role="img" aria-label="Green grass tuft"></span>Vegetable<br>garden creation</li>
    <li class="service-card col-right row-2"><span class="tuft" role="img" aria-label="Green grass tuft"></span>Green<br>waste removal</li>
    <li class="service-card col-left row-3"><span class="tuft" role="img" aria-label="Green grass tuft"></span>Pruning</li>
    <li class="service-card col-right row-3"><span class="tuft" role="img" aria-label="Green grass tuft"></span>Weeding</li>
  </ul>

  <section class="call-band">
    <span class="call-label">give us a call:</span>
    <span class="call-number">045 730 2864</span>
  </section>

  <div class="edge-stripe bottom"><span></span><span></span><span></span><span></span><span></span><span></span><span></span><span></span></div>
</main>
</body>
</html>
```